Trusty Hound Signage

This design is for "signage" that we intend to get produced.
A couple of different designs that say "Trusty Hound on Guard" and "Beware of Trusty Hound"
It should also have our logo (TH) plus our logo with the hand and dog paw. We would also like the main picture of the sign to be the attached. We would like a classy sophisticated look similar to our logo you designed.
Our designs will go on consumers gates/entrances to warn people there is a dog on the premises. I will get a better quality picture of the dog.
Look and feel
Each slider illustrates characteristics of the customer's brand and the style your logo design should communicate.

```html
<!DOCTYPE html>
<html lang="en">
<head>
<meta charset="utf-8">
<title>Trusty Hound Signage</title>
<link rel="stylesheet" href="https://fonts.googleapis.com/css2?family=Anton&display=swap">
<style>
  :root {
    --sign-yellow: #f9e814;
    --ink: #000000;
    --lavender: #9fa9d8;
    --dog-grey: #3d3d3d;
    --page: #ffffff;
  }
  html, body {
    margin: 0;
    padding: 0;
    width: 675px;
    height: 1200px;
    overflow: hidden;
    background: var(--page);
  }
  .canvas {
    position: relative;
    width: 675px;
    height: 1200px;
  }
  .sign {
    position: absolute;
    left: 104px;
    width: 466px;
    height: 465px;
    display: block;
  }
  .sign--on-guard { top: 97px; }
  .sign--beware { top: 638px; }
  .sign__headline {
    font-family: "Anton", "Arial Narrow", sans-serif;
    font-size: 62px;
    fill: var(--ink);
  }
  .sign__monogram {
    font-family: "Anton", "Arial Narrow", sans-serif;
    font-size: 120px;
    fill: var(--lavender);
  }
  .sign__brand {
    font-family: "Anton", "Arial Narrow", sans-serif;
    font-size: 82px;
    fill: var(--ink);
  }
</style>
</head>
<body>
<main class="canvas">

  <svg class="sign sign--on-guard" viewBox="0 0 745 744" role="group" aria-label="Trusty Hound on Guard sign">
    <rect class="sign__frame" x="0" y="0" width="745" height="744" fill="var(--ink)"/>
    <rect class="sign__hazard-band" x="16" y="16" width="713" height="712" fill="none" stroke="var(--sign-yellow)" stroke-width="10" stroke-dasharray="12 10"/>
    <rect class="sign__field" x="25" y="25" width="695" height="694" fill="var(--sign-yellow)"/>

    <g class="sign__badge">
      <circle cx="191" cy="178" r="137" fill="none" stroke="var(--ink)" stroke-width="2" stroke-dasharray="5 4"/>
      <circle cx="191" cy="178" r="125" fill="var(--ink)"/>
      <text class="sign__monogram" x="191" y="222" text-anchor="middle">TH</text>
    </g>

    <g class="sign__headline-block">
      <text class="sign__headline" x="688" y="115" text-anchor="end">TRUSTY HOUND</text>
      <text class="sign__headline" x="688" y="180" text-anchor="end">ON GUARD</text>
      <line x1="453" y1="200" x2="688" y2="200" stroke="var(--ink)" stroke-width="8" stroke-dasharray="22 14"/>
    </g>

    <polygon class="sign__dog-photo" role="img" aria-label="Photo of the seated guard dog" points="390,300 500,300 528,525 248,525" fill="var(--dog-grey)"/>
    <polygon class="sign__warning-triangle" points="373,213 193,528 553,528" fill="none" stroke="var(--ink)" stroke-width="10" stroke-linejoin="miter"/>

    <g class="sign__brand-line">
      <circle cx="124" cy="620" r="57" fill="none" stroke="var(--lavender)" stroke-width="4"/>
      <text class="sign__brand" x="200" y="650">Trusty Hound</text>
    </g>
  </svg>

  <svg class="sign sign--beware" viewBox="0 0 745 744" role="group" aria-label="Beware of Trusty Hound sign">
    <rect class="sign__frame" x="0" y="0" width="745" height="744" fill="var(--ink)"/>
    <rect class="sign__hazard-band" x="16" y="16" width="713" height="712" fill="none" stroke="var(--sign-yellow)" stroke-width="10" stroke-dasharray="12 10"/>
    <rect class="sign__field" x="25" y="25" width="695" height="694" fill="var(--sign-yellow)"/>

    <g class="sign__badge">
      <circle cx="191" cy="178" r="137" fill="none" stroke="var(--ink)" stroke-width="2" stroke-dasharray="5 4"/>
      <circle cx="191" cy="178" r="125" fill="var(--ink)"/>
      <text class="sign__monogram" x="191" y="222" text-anchor="middle">TH</text>
    </g>

    <g class="sign__headline-block">
      <text class="sign__headline" x="688" y="115" text-anchor="end">BEWARE OF</text>
      <text class="sign__headline" x="688" y="180" text-anchor="end">TRUSTY HOUND</text>
      <line x1="453" y1="200" x2="688" y2="200" stroke="var(--ink)" stroke-width="8" stroke-dasharray="22 14"/>
    </g>

    <polygon class="sign__dog-photo" role="img" aria-label="Photo of the seated guard dog" points="390,300 500,300 528,525 248,525" fill="var(--dog-grey)"/>
    <polygon class="sign__warning-triangle" points="373,213 193,528 553,528" fill="none" stroke="var(--ink)" stroke-width="10" stroke-linejoin="miter"/>

    <g class="sign__brand-line">
      <circle cx="124" cy="620" r="57" fill="none" stroke="var(--lavender)" stroke-width="4"/>
      <text class="sign__brand" x="200" y="650">Trusty Hound</text>
    </g>
  </svg>

</main>
</body>
</html>
```